Geschäftspapiere für Kanzlei
Zielgruppe
Forschungsinstitute und Großunternehmen die eigene Entwicklungsabteilungen haben und Erfindungen patentieren lassen.
Aufgabenstellung
Möglicherweise ergibt eine Weiterentwiklung unseres logos Sinn? Denkbar wäre für uns aber auch auf das Logo ganz zu verzichten.
Es sollte nicht mehr als eine Farbe (Blauton) verwendet werden. Wir wollen schlicht, klassisch und seriös auftreten.

```html
<!DOCTYPE html>
<html lang="de">
<head>
<meta charset="utf-8">
<title>Briefbogen – Kanzlei Dr. Veskoni</title>
<link href="https://fonts.googleapis.com/css2?family=Montserrat:wght@400;600;700&display=swap" rel="stylesheet">
<style>
  :root {
    --blue: #2f72bd;
    --ink: #222222;
    --faint-blue: #e0e9f4;
    --paper: #ffffff;
  }
  * { margin: 0; padding: 0; box-sizing: border-box; }
  html, body { width: 849px; height: 1200px; overflow: hidden; background: var(--paper); }
  body { font-family: "Montserrat", sans-serif; color: var(--ink); position: relative; }
  .sheet { position: relative; width: 849px; height: 1200px; border: 1px solid #d6d6d6; }

  .brand { position: absolute; left: 96px; top: 44px; display: flex; align-items: flex-end; gap: 20px; }
  .brand-square { width: 80px; height: 84px; background: var(--blue); }
  .brand-text { padding-bottom: 0; line-height: 1.2; }
  .brand-name { font-weight: 600; font-size: 15.5px; color: var(--ink); }
  .brand-sub { font-weight: 400; font-size: 15px; color: var(--ink); letter-spacing: 0.2px; }

  .rule { position: absolute; left: 97px; width: 712px; height: 1px; background: var(--blue); }
  .rule-head { top: 165px; }
  .rule-foot-top { top: 1117px; }
  .rule-foot-bottom { top: 1162px; }

  .sender-line { position: absolute; left: 96px; top: 201px; font-size: 9px; }
  .sender-line strong { color: var(--blue); font-weight: 600; }

  .contact { position: absolute; left: 591px; top: 199px; font-size: 10.2px; line-height: 12.7px; }
  .contact p { margin-bottom: 9px; }
  .contact .name { color: var(--blue); font-weight: 700; }
  .contact b { font-weight: 700; }
  .contact .label { display: inline-block; width: 44px; font-weight: 700; }
  .contact .bank-label { display: inline-block; width: 36px; }

  .fold { position: absolute; left: 20px; width: 29px; height: 1px; }
  .fold-1 { top: 423px; background: var(--blue); }
  .fold-2 { top: 599px; background: var(--ink); }

  .watermark { position: absolute; left: 0; width: 849px; top: 760px; text-align: center;
    font-weight: 700; font-size: 64px; color: var(--faint-blue); letter-spacing: 1px; }

  .web { position: absolute; left: 97px; width: 712px; top: 1128px; text-align: center; font-size: 17px; letter-spacing: 0.3px; }
</style>
</head>
<body>
<div class="sheet">
  <header class="brand">
    <div class="brand-square"></div>
    <div class="brand-text">
      <div class="brand-name">Dr. Tamar Veskoni</div>
      <div class="brand-sub">Patentanwaltskanzlei</div>
    </div>
  </header>
  <div class="rule rule-head"></div>

  <div class="sender-line"><strong>Kanzlei Dr. Veskoni</strong> · Lindenhofstrasse 22 · 80639 München</div>

  <aside class="contact">
    <p><span class="name">Dr. rer. nat. Tamar Veskoni, PhD</span><br>
      <b>Patentanwalt</b><br>
      European Patent Attorney<br>
      European Design- und Trademark Attorney</p>
    <p>Lindenhofstrasse 22<br>80639 München</p>
    <p><span class="label">Telefon:</span>+49 89 400 318 270<br>
      <span class="label">Telefax:</span>+49 89 400 318 29<br>
      <span class="label">E-Mail:</span>office@veskoni.de</p>
    <p><span class="label">St.-Nr.:</span>143/208/51937</p>
    <p><b>Isartal Bank</b><br>
      <span class="bank-label">Konto:</span>3051847260<br>
      <span class="bank-label">IBAN:</span>DE12700200003051847260<br>
      <span class="bank-label">BIC:</span>ISTBDEM1XXX</p>
  </aside>

  <div class="fold fold-1"></div>
  <div class="fold fold-2"></div>

  <div class="watermark" aria-hidden="true">Dr. Tamar Veskoni</div>

  <div class="rule rule-foot-top"></div>
  <footer class="web">www.veskoni.de</footer>
  <div class="rule rule-foot-bottom"></div>
</div>
</body>
</html>
```